Insect-based foods company needs bright, eye catching pouch design for its Green Flour Blend

We are a UK based cricket farm called Molten Acre (www.moltenacre-example.com) and have a retail brand called 'Hoplume' (www.hoplume-example.com). Our main product is 'Green Flour Blend' which we already sell wholesale, through the Hoplume website and on Tradevo UK. At the moment we have designed our own labels which we stick on stand up pouches. This does not look very professional and is very time consuming to do. We are looking to have our pouches custom printed instead and want a new, bold design. We want a design that is bright, colourful, and eye-catching. Our packaging needs to stand out and make the statement - 'this is not an ordinary protein powder'. A few key points:
1. The pouches measure 130mm*225mm
2. We want to keep our existing 'Hoplume' logo
3. We need a design for the front and back. Please use our existing text for the basis of the back of the pack but change it as you see fit.
4. We would like the Union Jack flag to show prominently. Ours is the only cricket powder on the market which is made in the UK and we want to make a big deal about this.
5. The packaging needs to grab peoples attention on the shelf and also on the Tradevo search results page.
6. We intend to use the style of the packaging to re-design our website to match it. This means the theme of the packaging needs to translate well to the overall look of the website.

Target Market(s)

Younger people looking for exiting new protein powder which is sustainable and healthy. Would like to appeal to both men and women.

Font styles to use
Sans Serif

Requirements
Must have
• 1. The pouches measure 130mm*225mm
3. We need a design for the front and back.
4. We would like the Union Jack flag to show somewhere on the packaging. Ours is the only cricket powder on the market which is made in the UK and we want to make a big deal about this.

```html
<!DOCTYPE html>
<html lang="en">
<head>
<meta charset="utf-8">
<title>Hoplume – Green Flour Blend pouch front</title>
<link rel="stylesheet" href="https://fonts.googleapis.com/css2?family=Arimo:wght@400;700&family=Oswald:wght@600;700&display=swap">
<style>
  :root {
    --paper: #ffffff;
    --frame: #231f20;
    --band-grey: #d1d2d4;
    --panel-grey: #e6e7e8;
    --brand-red: #ed1c24;
    --deep-red: #da1a21;
    --ink: #231f20;
    --signal-yellow: #fff200;
    --flag-blue: #1b2a6b;
    --flag-red: #d21f2b;
  }
  * { margin: 0; padding: 0; box-sizing: border-box; }
  html, body { width: 785px; height: 1200px; overflow: hidden; background: var(--paper); }
  .canvas { position: relative; width: 785px; height: 1200px; }
  .pouch-art { position: absolute; left: 0; top: 0; }

  .brand-name {
    position: absolute; left: 189px; top: 306px;
    font-family: "Arimo", Arial, sans-serif; font-weight: 700;
    font-size: 54px; line-height: 70px; color: var(--paper);
    letter-spacing: -1px;
  }
  .strap {
    position: absolute; font-family: "Oswald", "Arial Narrow", sans-serif;
    font-weight: 600; color: var(--signal-yellow); line-height: 1;
    letter-spacing: 0.5px;
  }
  .strap--top { left: 189px; top: 449px; font-size: 28px; }
  .strap--bottom { left: 160px; top: 858px; font-size: 28px; letter-spacing: 1px; }

  .product-name {
    position: absolute; left: 190px; top: 500px;
    font-family: "Oswald", "Arial Narrow", sans-serif; font-weight: 700;
    font-size: 114px; line-height: 112px; color: var(--paper);
    text-transform: uppercase; text-shadow: 2px 2px 0 var(--ink);
  }
  .product-name span { display: block; }

  .pack-facts {
    position: absolute; left: 159px; top: 988px;
    font-family: "Arimo", Arial, sans-serif; font-size: 15px; line-height: 21px;
    color: var(--paper);
  }
  .origin {
    position: absolute; left: 316px; top: 1014px;
    font-family: "Arimo", Arial, sans-serif; font-size: 15px; color: var(--paper);
  }
  .union-flag { position: absolute; left: 343px; top: 965px; }
</style>
</head>
<body>
<main class="canvas">
  <svg class="pouch-art" width="785" height="1200" viewBox="0 0 785 1200" aria-hidden="true">
    <rect class="pouch-frame" x="108.5" y="110.5" width="563" height="988" fill="var(--paper)" stroke="var(--frame)" stroke-width="1"/>
    <rect class="seal-band" x="109" y="224" width="562" height="36" fill="var(--band-grey)"/>
    <polygon class="side-panel" points="671,260 267,671 671,1081" fill="var(--panel-grey)"/>
    <polygon class="logo-band" points="109,304 500,304 417,387 109,387" fill="var(--brand-red)"/>
    <polygon class="strap-band" points="108,447 486,447 450,485 108,485" fill="var(--ink)"/>
    <rect class="hero-band" x="108" y="485" width="564" height="371" fill="var(--brand-red)"/>
    <polygon class="hero-shade" points="450,485 672,485 672,856 450,856 267,671" fill="var(--deep-red)"/>
    <polygon class="strap-band" points="108,856 450,856 486,893 108,893" fill="var(--ink)"/>
    <polygon class="facts-band" points="109,953 417,953 500,1036 109,1036" fill="var(--brand-red)"/>
  </svg>

  <div class="brand-name">hoplume</div>
  <div class="strap strap--top">ULTRAFINE ROASTED</div>
  <h1 class="product-name"><span>Green</span><span>Flour</span><span>Blend</span></h1>
  <div class="strap strap--bottom">SIX-LEGGED SUPERFOOD</div>

  <div class="pack-facts">100g &#8494;<br>Approx. 10 servings</div>
  <svg class="union-flag" width="67" height="45" viewBox="0 0 60 40" preserveAspectRatio="none" role="img" aria-label="Union flag">
    <defs><clipPath id="flag-clip"><rect width="60" height="40"/></clipPath></defs>
    <g clip-path="url(#flag-clip)">
      <rect width="60" height="40" fill="var(--flag-blue)"/>
      <path d="M0,0 L60,40 M60,0 L0,40" stroke="var(--paper)" stroke-width="8"/>
      <path d="M0,0 L60,40 M60,0 L0,40" stroke="var(--flag-red)" stroke-width="2.6"/>
      <path d="M30,0 V40 M0,20 H60" stroke="var(--paper)" stroke-width="12"/>
      <path d="M30,0 V40 M0,20 H60" stroke="var(--flag-red)" stroke-width="6"/>
    </g>
  </svg>
  <div class="origin">Farmed in the UK</div>
</main>
</body>
</html>
```